Business card for Eyelash extension salon in Beverly Hills,California USA

We need new business card for our salon in Beverly Hills. The salon name is 'Lashvora' . We would like to have...Business name: Lashvora Name of person: will provide later Address 6812 N.Calder Ridge Ave Beverly Hills , CA 90210 Phone: will provide later (Text only) Web: www.lashvorastudio-demo.com Instagram icon, Facebook icon follow us for seasonal campaign and news @lashvorastudiodemo Design should look elegant, high-end, clean, simple, cohesive with my brand. Please refer my brand board. Business name color will be metallic bronzy color. Im thinking grey background or white background. Thanks

Target Market(s)

25-35. Gender neutral. People who are in Entertainment business industry.
This is High-end Eyelash extension salon in Beverly Hills

Industry/Entity Type

Beauty Salon

Contact Information for Business Card

Business name: Lashvora
Name of person: will provide later
Address 6812 N.Calder Ridge Ave Beverly Hills , CA 90210
Phone: will provide later (Text only)
Web: www.lashvorastudio-demo.com
Instagram icon, Facebook icon
follow us for seasonal campaign and news @lashvorastudiodemo

Requirements
Must have
• Beautiful, elegant, clean and simple look but very attractive and modern
Should not have
• We don't like too clutter, too busy designs.

```html
<!DOCTYPE html>
<html lang="en">
<head>
<meta charset="utf-8">
<title>Lashvora Business Card</title>
<link href="https://fonts.googleapis.com/css2?family=Josefin+Sans:wght@300;400&family=Cormorant+Garamond:ital,wght@1,500&display=swap" rel="stylesheet">
<style>
  :root {
    --page: #e6e4e1;
    --card: #7b4128;
    --card-edge: #5e2f1c;
    --foil: #dcbc72;
    --foil-soft: #c9a55e;
  }
  * { margin: 0; padding: 0; box-sizing: border-box; }
  html, body { width: 1200px; height: 1021px; overflow: hidden; background: var(--page); }
  .sheet {
    width: 1200px; height: 1021px;
    display: flex; flex-direction: column; align-items: center; justify-content: center; gap: 56px;
  }
  .card {
    position: relative;
    width: 700px; height: 400px;
    background: var(--card);
    border-radius: 4px;
    box-shadow: 0 2px 0 var(--card-edge), 0 14px 30px rgba(0,0,0,0.18);
    color: var(--foil);
    font-family: 'Josefin Sans', sans-serif;
  }
  .wordmark { font-family: 'Josefin Sans', sans-serif; font-weight: 300; color: var(--foil); line-height: 1; }
  .locale { font-size: 9px; letter-spacing: 2px; color: var(--foil); }

  /* Front */
  .card-front .brand { position: absolute; left: 0; right: 0; top: 132px; text-align: center; }
  .card-front .wordmark { font-size: 74px; letter-spacing: 2px; }
  .card-front .locale { position: absolute; left: 430px; top: 215px; font-size: 10px; }
  .card-front .site { position: absolute; left: 0; right: 0; top: 262px; text-align: center; font-size: 17px; letter-spacing: 1.5px; color: var(--foil-soft); }

  /* Back */
  .card-back .brand { position: absolute; left: 60px; top: 160px; }
  .card-back .wordmark { font-size: 52px; letter-spacing: 1px; }
  .card-back .locale { display: block; text-align: right; margin-top: 8px; font-size: 8px; }
  .person { position: absolute; left: 370px; top: 66px; }
  .person .name { font-family: 'Cormorant Garamond', serif; font-style: italic; font-weight: 500; font-size: 26px; line-height: 1; }
  .person .role { font-size: 12px; margin-top: 2px; color: var(--foil-soft); }
  .contacts { list-style: none; margin-top: 12px; }
  .contacts li { display: flex; align-items: center; gap: 9px; font-size: 12.5px; height: 22px; letter-spacing: 0.3px; }
  .contacts svg { width: 13px; height: 13px; flex: none; }
  .address { position: absolute; left: 60px; bottom: 44px; display: flex; align-items: center; gap: 7px; font-size: 13.5px; letter-spacing: 0.3px; }
  .address svg { width: 11px; height: 14px; }
</style>
</head>
<body>
<main class="sheet">
  <section class="card card-front" aria-label="Card front">
    <div class="brand"><span class="wordmark">Lashvora</span></div>
    <span class="locale">BEVERLY HILLS</span>
    <p class="site">www.lashvorastudio-demo.com</p>
  </section>

  <section class="card card-back" aria-label="Card back">
    <div class="brand">
      <span class="wordmark">Lashvora</span>
      <span class="locale">BEVERLY HILLS</span>
    </div>
    <div class="person">
      <p class="name">Your Name</p>
      <p class="role">job title</p>
      <ul class="contacts">
        <li><svg viewBox="0 0 14 14" fill="none" stroke="#dcbc72" stroke-width="1.2"><path d="M2 4c0-1 1-2 2-2h6c1 0 2 1 2 2v1H9V4H5v1H2z"/><rect x="3" y="6" width="8" height="6" rx="1"/></svg>000 000 0000</li>
        <li><svg viewBox="0 0 14 14" fill="none" stroke="#dcbc72" stroke-width="1.2"><rect x="1.5" y="3" width="11" height="8"/><path d="M1.5 3l5.5 4.5L12.5 3"/></svg>youremail@lashvora-demo.com</li>
        <li><svg viewBox="0 0 14 14" fill="none" stroke="#dcbc72" stroke-width="1.2"><circle cx="7" cy="7" r="5.5"/><ellipse cx="7" cy="7" rx="2.4" ry="5.5"/><path d="M1.5 7h11"/></svg>www.lashvorastudio-demo.com</li>
        <li><svg viewBox="0 0 14 14" fill="none" stroke="#dcbc72" stroke-width="1.2"><rect x="2" y="2" width="10" height="10"/></svg>@lashvorastudiodemo</li>
      </ul>
    </div>
    <p class="address"><svg viewBox="0 0 11 14" fill="#dcbc72"><path d="M5.5 0C2.5 0 0 2.4 0 5.4 0 9.2 5.5 14 5.5 14S11 9.2 11 5.4C11 2.4 8.5 0 5.5 0zm0 7.4a2 2 0 110-4 2 2 0 010 4z"/></svg>6812 N.Calder Ridge Ave Beverly Hills , CA 90210</p>
  </section>
</main>
</body>
</html>
```